Bright Arrow Delivery Service Wordpress design

My client is a delivery service whose motto is "We go where the freight leads us." Their colors are red, white and blue. They use Voyalo vans and box vans - NO semi tractors. They like this Website design www.tovamu-sample.com, but I would like to see some designs that make them stand out. Attached is their new logo.

Target Market(s)

Businesses who use delivery services in town and anyone needing freight picked up or transported in the United States.

Industry/Entity Type

Delivery Service

Number of Pages Required

1 page

Font styles to use
Sans Serif

Colors
ec1f27
0455a3
ffffff

Requirements
Must have
• We need a Wordpress design with sliders that incorporates their new logo and the motto "WE GO WHERE THE FREIGHT LEADS US" Their corporate colors are red, white and blue. They only use voyalo vans and box vans.
Nice to have
• Please use your creativity to come up with a unique design for this delivery service.
Should not have
• NO SEMI TRACTOR TRAILERS

```html
<!DOCTYPE html>
<html lang="en">
<head>
<meta charset="utf-8">
<title>Bright Arrow Delivery Service</title>
<link href="https://fonts.googleapis.com/css2?family=Montserrat:wght@700;800&family=Open+Sans:wght@400;600;700&family=Lato:wght@700;900&display=swap" rel="stylesheet">
<style>
  :root {
    --brand-blue: #0455a3;
    --brand-red: #ec1f27;
    --white: #ffffff;
    --header-bg: #f4f4f4;
    --nav-line: #d9d9d9;
    --footer-bg: #1f1f1f;
    --footer-text: #e6e6e6;
  }
  * { box-sizing: border-box; margin: 0; padding: 0; }
  html, body { width: 919px; height: 1200px; overflow: hidden; background: var(--white); }
  body { position: relative; font-family: "Open Sans", sans-serif; }

  .site-header { position: absolute; left: 0; top: 0; width: 919px; height: 80px; background: var(--header-bg); border-bottom: 1px solid var(--nav-line); }
  .brand { position: absolute; left: 90px; top: 24px; display: flex; align-items: center; gap: 8px; }
  .brand-mark { width: 14px; height: 14px; border-radius: 50%; background: var(--brand-red); }
  .brand-name { font-family: "Montserrat", sans-serif; font-weight: 800; font-size: 14px; color: var(--brand-blue); line-height: 1; }
  .main-nav { position: absolute; top: 0; left: 420px; height: 80px; display: flex; }
  .main-nav a { display: flex; align-items: center; justify-content: center; height: 80px; font-size: 10px; color: var(--brand-blue); text-decoration: none; border-right: 1px solid var(--nav-line); }
  .main-nav a.is-active { background: var(--brand-blue); color: var(--white); font-weight: 700; letter-spacing: .5px; border-right: none; }
  .nav-home { width: 68px; } .nav-about { width: 69px; } .nav-services { width: 79px; } .nav-carrers { width: 62px; } .nav-contact { width: 67px; }
  .login { position: absolute; left: 802px; top: 33px; font-size: 10px; color: var(--brand-blue); display: flex; align-items: center; gap: 4px; }

  .hero { position: absolute; left: 0; top: 80px; width: 919px; height: 416px; background: linear-gradient(100deg, #9a9a98 0%, #7d7d7b 45%, #a2a2a0 100%); }
  .hero-title { position: absolute; top: 82px; width: 919px; text-align: center; font-family: "Montserrat", sans-serif; font-weight: 800; font-size: 29px; color: var(--white); letter-spacing: 1px; text-shadow: 0 2px 4px rgba(0,0,0,.45); }
  .hero-text { position: absolute; left: 212px; top: 150px; width: 495px; font-size: 13px; line-height: 15.5px; text-align: justify; text-align-last: center; color: var(--white); text-shadow: 0 1px 2px rgba(0,0,0,.5); }
  .slider-dots { position: absolute; left: 896px; top: 111px; display: flex; flex-direction: column; gap: 9px; }
  .slider-dots span { width: 3px; height: 32px; background: rgba(255,255,255,.45); }
  .slider-dots span.is-current { background: var(--white); }

  .services { position: absolute; left: 74px; top: 339px; display: flex; gap: 12px; }
  .service-card { width: 184px; height: 225px; background: var(--brand-blue); color: var(--white); text-align: center; position: relative; }
  .service-icon { position: absolute; left: 52px; top: 20px; width: 80px; height: 98px; border-radius: 8px; }
  .service-title { position: absolute; top: 132px; width: 100%; font-family: "Montserrat", sans-serif; font-weight: 800; font-size: 18px; letter-spacing: .5px; }
  .service-text { position: absolute; top: 157px; left: 22px; width: 140px; font-size: 7px; line-height: 8.5px; }
  .service-more { position: absolute; top: 193px; left: 45px; width: 87px; height: 20px; border: 1px solid var(--white); font-family: "Montserrat", sans-serif; font-weight: 700; font-size: 12px; line-height: 18px; }

  .what-we-do { position: absolute; top: 588px; left: 0; width: 919px; text-align: center; }
  .what-we-do h2 { font-family: "Montserrat", sans-serif; font-weight: 800; font-size: 18px; color: var(--brand-blue); }
  .what-we-do p { width: 370px; margin: 14px auto 0; font-size: 10px; line-height: 12px; color: var(--brand-blue); }

  .about { position: absolute; left: 79px; top: 716px; width: 762px; height: 273px; overflow: hidden; }
  .about-photo { position: absolute; inset: 0; background: linear-gradient(110deg, #b49a4c 0%, #e8d7aa 40%, #f1ead9 70%, #d9d4cf 100%); }
  .about-panel { position: absolute; inset: 0; }
  .about h2 { position: absolute; left: 41px; top: 86px; font-family: "Montserrat", sans-serif; font-weight: 800; font-size: 22px; color: var(--white); }
  .about p { position: absolute; left: 39px; top: 138px; font-size: 14px; line-height: 17.2px; color: var(--white); letter-spacing: .3px; white-space: nowrap; }

  .site-footer { position: absolute; left: 0; top: 1025px; width: 919px; height: 175px; background: var(--footer-bg); color: var(--footer-text); }
  .footer-heading { position: absolute; font-family: "Lato", sans-serif; font-weight: 900; font-size: 16px; color: var(--white); letter-spacing: -.2px; }
  .newsletter-heading { left: 79px; top: 34px; }
  .nav-heading { left: 368px; top: 24px; letter-spacing: .5px; }
  .follow-heading { left: 605px; top: 24px; }
  .email-input { position: absolute; left: 79px; top: 71px; width: 138px; height: 21px; background: #ececec; border: 1px solid #bbb; }
  .subscribe { position: absolute; left: 221px; top: 71px; width: 57px; height: 21px; border: 1px solid var(--white); font-size: 8px; font-weight: 700; color: var(--white); text-align: center; line-height: 19px; }
  .email-note { position: absolute; left: 79px; top: 96px; font-size: 8px; }
  .footer-links { position: absolute; left: 368px; top: 55px; list-style: none; }
  .footer-links li { font-size: 9px; height: 19px; display: flex; align-items: center; gap: 12px; }
  .social { position: absolute; left: 605px; top: 57px; display: flex; gap: 14px; }
  .social span { width: 36px; height: 36px; }
  .s1 { background: #2b5ca8; } .s2 { background: #1da1f2; } .s3 { background: #e2402f; } .s4 { background: #e24a2c; }
</style>
</head>
<body>
  <header class="site-header">
    <div class="brand"><span class="brand-mark"></span><span class="brand-name">Bright Arrow Delivery</span></div>
    <nav class="main-nav">
      <a class="nav-home is-active" href="#">HOME</a>
      <a class="nav-about" href="#">ABOUT</a>
      <a class="nav-services" href="#">SERVICES</a>
      <a class="nav-carrers" href="#">CARRERS</a>
      <a class="nav-contact" href="#">CONTACT</a>
    </nav>
    <div class="login">
      <svg width="10" height="11" viewBox="0 0 10 11" fill="none" stroke="currentColor" stroke-width="1"><path d="M5 1h4v9H5M1 5.5h5M4 3.5l2 2-2 2"/></svg>
      LOGIN
    </div>
  </header>

  <section class="hero" role="img" aria-label="Photo of a courier in work clothes running with a cardboard box against a concrete wall">
    <h1 class="hero-title">WE GO WHERE THE FREIGHT LEADS US</h1>
    <p class="hero-text">Lorem ipsum dolor sit amet, consectetur adipiscing elit. Duis vestibulum ipsum nisl, in elementum lectus scelerisque a. Sed egestas sagittis nisl. Ut at convallis justo. Mauris vestibulum eu augue sit amet sodales. Ut elementum ac magna non commodo.</p>
    <div class="slider-dots"><span></span><span class="is-current"></span><span></span><span></span><span></span></div>
  </section>

  <section class="services">
    <article class="service-card">
      <div class="service-icon" role="img" aria-label="Illustration of a delivery courier in a cap" style="background:#f0674a"></div>
      <h3 class="service-title">SERVICE 1</h3>
      <p class="service-text">Lorem ipsum dolor sit amet, consectetur adipiscing elit. Duis vestibulum ipsum.</p>
      <div class="service-more">More</div>
    </article>
    <article class="service-card">
      <div class="service-icon" role="img" aria-label="Illustration of a 24 hour clock" style="background:#e9423a;border-radius:50%;height:80px;top:28px"></div>
      <h3 class="service-title">SERVICE 2</h3>
      <p class="service-text">Lorem ipsum dolor sit amet, consectetur adipiscing elit. Duis vestibulum ipsum.</p>
      <div class="service-more">More</div>
    </article>
    <article class="service-card">
      <div class="service-icon" role="img" aria-label="Illustration of a clipboard" style="background:#f9a12b;left:63px;width:58px;border-radius:2px"></div>
      <h3 class="service-title">SERVICE 3</h3>
      <p class="service-text">Lorem ipsum dolor sit amet, consectetur adipiscing elit. Duis vestibulum ipsum.</p>
      <div class="service-more">More</div>
    </article>
    <article class="service-card">
      <div class="service-icon" role="img" aria-label="Illustration of a hand truck carrying a crate" style="background:#fbd9a6"></div>
      <h3 class="service-title">SERVICE 4</h3>
      <p class="service-text">Lorem ipsum dolor sit amet, consectetur adipiscing elit. Duis vestibulum ipsum.</p>
      <div class="service-more">More</div>
    </article>
  </section>

  <section class="what-we-do">
    <h2>What We Do</h2>
    <p>Lorem ipsum dolor sit amet, consectetur adipiscing elit. Duis vestibulum ipsum nisl, in elementum lectus scelerisque a. Sed egestas sagittis nisl. Ut at convallis justo. Mauris vestibulum eu augue sit amet sodales. Ut elementum ac magna non commodo.</p>
  </section>

  <section class="about">
    <div class="about-photo" role="img" aria-label="Photo of a white delivery van driving on a sunlit country road"></div>
    <svg class="about-panel" width="762" height="273" viewBox="0 0 762 273"><polygon points="0,2 762,273 0,273" fill="var(--brand-blue)"/></svg>
    <h2>About Us</h2>
    <p>Lorem ipsum dolor sit amet, con-<br>sectetur adipiscing elit. Duis vestibulum<br>ipsum nisl, in elementum lectus scelerisque a.<br>Sed egestas sagittis nisl. Ut at convallis justo. Mauris<br>vestibulum eu augue sit amet sodales. Ut elementum ac<br>magna non commodo.</p>
  </section>

  <footer class="site-footer">
    <h4 class="footer-heading newsletter-heading">GET OUR NEWSLETTER</h4>
    <div class="email-input"></div>
    <div class="subscribe">SUBCRIBE</div>
    <p class="email-note">*please, insert your email</p>

    <h4 class="footer-heading nav-heading">NAVIGATION</h4>
    <ul class="footer-links">
      <li><svg width="6" height="8" viewBox="0 0 6 8"><path d="M1 1l3 3-3 3" stroke="#1e8de0" stroke-width="1.6" fill="none"/></svg>HOME</li>
      <li><svg width="6" height="8" viewBox="0 0 6 8"><path d="M1 1l3 3-3 3" stroke="#1e8de0" stroke-width="1.6" fill="none"/></svg>ABOUT US</li>
      <li><svg width="6" height="8" viewBox="0 0 6 8"><path d="M1 1l3 3-3 3" stroke="#1e8de0" stroke-width="1.6" fill="none"/></svg>SERVICES</li>
      <li><svg width="6" height="8" viewBox="0 0 6 8"><path d="M1 1l3 3-3 3" stroke="#1e8de0" stroke-width="1.6" fill="none"/></svg>CARRERS</li>
      <li><svg width="6" height="8" viewBox="0 0 6 8"><path d="M1 1l3 3-3 3" stroke="#1e8de0" stroke-width="1.6" fill="none"/></svg>CONTACT US</li>
    </ul>

    <h4 class="footer-heading follow-heading">FOLLOW US</h4>
    <div class="social"><span class="s1"></span><span class="s2"></span><span class="s3"></span><span class="s4"></span></div>
  </footer>
</body>
</html>
```